Corporate PowerPoint Template

Seeking a Powerpoint Template Design for High Technology company based in Silicon Valley. We are seeking a general template design that conveys a professional, clean, progressive message.

The Template must have the following elements at a minimum:
1. Title Page (see comments following)
2. Agenda Page
3. Page Number, Date and Confidentiality Statement
Items in #3 are to appear on all pages except title page

We expect the Title page to be graphical in nature with area for Presentation Title, Presenter Name, Date and a place for confidentiality statement should be present as well. Three (3) distinct Title pages to address different constituencies: Customers, Partners and Internal Communications.

In general, we would like to stay with our corporate color scheme (which may be found in our logo). To better understand our products, logo and look and feel - please visit our website at: http://www.velmarotek.example

```html
<!DOCTYPE html>
<html lang="en">
<head>
<meta charset="utf-8">
<title>Velmarotek Slide Template</title>
<link rel="stylesheet" href="https://fonts.googleapis.com/css2?family=Roboto+Condensed:wght@300;400&family=Open+Sans:wght@400;700&display=swap">
<style>
  :root {
    --teal: #1a8c9c;
    --teal-footer: #38868f;
    --body-grey: #8a8a8a;
    --header-top: #f2f2f2;
    --white: #ffffff;
  }
  html, body {
    margin: 0;
    padding: 0;
    overflow: hidden;
    background: var(--white);
  }
  .slide {
    position: relative;
    width: 1200px;
    height: 900px;
    overflow: hidden;
    background: var(--white);
    font-family: "Roboto Condensed", "Arial Narrow", sans-serif;
  }
  .slide-header {
    position: absolute;
    left: 0; top: 0;
    width: 1200px; height: 117px;
    background: linear-gradient(to bottom, var(--header-top), var(--white));
    box-shadow: 0 2px 4px rgba(0,0,0,0.06);
  }
  .project-title {
    position: absolute;
    left: 44px; top: 24px;
    margin: 0;
    font-size: 46px;
    font-weight: 400;
    color: var(--teal);
    letter-spacing: 0.5px;
  }
  .brand {
    position: absolute;
    right: 22px; top: 18px;
    display: flex;
    align-items: center;
    gap: 16px;
  }
  .brand-mark {
    width: 64px; height: 64px;
  }
  .brand-name {
    font-size: 50px;
    font-weight: 400;
    color: var(--teal);
    letter-spacing: 1px;
  }
  .column {
    position: absolute;
    top: 190px;
    width: 500px;
  }
  .column-left { left: 54px; }
  .column-right { left: 626px; }
  .column-heading {
    margin: 0 0 26px;
    font-size: 36px;
    font-weight: 400;
    color: var(--teal);
    line-height: 44px;
  }
  .column-text {
    margin: 0 0 34px;
    font-size: 21px;
    font-weight: 300;
    color: var(--body-grey);
    line-height: 34.5px;
  }
  .column-text span {
    display: block;
    white-space: nowrap;
  }
  .slide-footer {
    position: absolute;
    left: 0; bottom: 0;
    width: 1200px; height: 54px;
    background: var(--teal-footer);
    font-family: "Open Sans", Arial, sans-serif;
    color: var(--white);
    font-size: 19px;
  }
  .copyright {
    position: absolute;
    left: 20px; top: 14px;
  }
  .page-number {
    position: absolute;
    right: 16px; top: 14px;
    font-weight: 700;
  }
</style>
</head>
<body>
<div class="slide">
  <header class="slide-header">
    <h1 class="project-title">PROJECT TITLE HERE</h1>
    <div class="brand">
      <svg class="brand-mark" viewBox="0 0 64 64" aria-hidden="true">
        <circle cx="32" cy="32" r="28" fill="var(--teal)"/>
      </svg>
      <span class="brand-name">velmarotek</span>
    </div>
  </header>

  <section class="column column-left">
    <h2 class="column-heading">SUBTEXT HERE</h2>
    <p class="column-text">
      <span>Subtxt here Subtxt here Subtxt here Subtxt here Subtxt here</span>
      <span>Subtxt here Subtxt here Subtxt here Subtxt here Subtxt here</span>
      <span>Subtxt here Subtxt here Subtxt here Subtxt here Subtxt here</span>
      <span>Subtxt here Subtxt here Subtxt here Subtxt here Subtxt here</span>
      <span>Subtxt here Subtxt here Subtxt here Subtxt here Subtxt here</span>
      <span>Subtxt here Subtxt here Subtxt here Subtxt here Subtxt here</span>
      <span>Subtxt here Subtxt here</span>
    </p>
    <p class="column-text">
      <span>Subtxt here Subtxt here Subtxt here Subtxt here Subtxt here</span>
      <span>Subtxt here Subtxt here Subtxt here Subtxt here Subtxt here</span>
      <span>Subtxt here Subtxt here Subtxt here Subtxt here Subtxt here</span>
      <span>Subtxt here Subtxt here Subtxt here Subtxt here Subtxt here</span>
      <span>Subtxt here Subtxt here Subtxt here Subtxt here Subtxt here</span>
      <span>Subtxt here Subtxt here Subtxt here Subtxt here Subtxt here</span>
      <span>Subtxt here Subtxt here</span>
    </p>
  </section>

  <section class="column column-right">
    <h2 class="column-heading">SUBTEXT HERE</h2>
    <p class="column-text">
      <span>Subtxt here Subtxt here Subtxt here Subtxt here Subtxt here</span>
      <span>Subtxt here Subtxt here Subtxt here Subtxt here Subtxt here</span>
      <span>Subtxt here Subtxt here Subtxt here Subtxt here Subtxt here</span>
      <span>Subtxt here Subtxt here Subtxt here Subtxt here Subtxt here</span>
      <span>Subtxt here Subtxt here Subtxt here Subtxt here Subtxt here</span>
      <span>Subtxt here Subtxt here Subtxt here Subtxt here Subtxt here</span>
      <span>Subtxt here Subtxt here</span>
    </p>
    <p class="column-text">
      <span>Subtxt here Subtxt here Subtxt here Subtxt here Subtxt here</span>
      <span>Subtxt here Subtxt here Subtxt here Subtxt here Subtxt here</span>
      <span>Subtxt here Subtxt here Subtxt here Subtxt here Subtxt here</span>
      <span>Subtxt here Subtxt here Subtxt here Subtxt here Subtxt here</span>
      <span>Subtxt here Subtxt here Subtxt here Subtxt here Subtxt here</span>
      <span>Subtxt here Subtxt here Subtxt here Subtxt here Subtxt here</span>
      <span>Subtxt here Subtxt here</span>
    </p>
  </section>

  <footer class="slide-footer">
    <span class="copyright">Copyright text here</span>
    <span class="page-number">Page : 01</span>
  </footer>
</div>
</body>
</html>
```